依頼詳細
■入れてほしい文言
エクセルデータ参照してください

■ のぼり、ポスターサイズ情報
サイズ:横600mm×縦1800mm以内

■ デザインへの要望
洋風調、和風調 のぼりデザインを作成したい
デザイン参考に添付ファイルの画像を参照
記載項目
サイズ:横600mm×縦1800mm以内
希望イメージ
シンプル 複雑
単色 カラフル
暗い 明るい
日常 高級
遊び心 厳粛
未来的 伝統的
女性的 男性的
希望する色
納品ファイル
• イラストレーター形式 (.ai)
• フォトショップ形式 (.psd)
• PNG形式 (.png)
補足説明

```html
<!DOCTYPE html>
<html lang="ja">
<head>
<meta charset="utf-8">
<title>山城建具組合 のぼり</title>
<link rel="stylesheet" href="https://fonts.googleapis.com/css2?family=M+PLUS+1p:wght@300;400&display=swap">
<style>
  :root {
    --banner-red: #7b1d24;
    --label-tan: #dcb79c;
    --photo-dark: #3a2516;
    --photo-mid: #8a5a3a;
    --photo-light: #c79a72;
  }
  * { margin: 0; padding: 0; box-sizing: border-box; }
  html, body {
    width: 1200px;
    height: 3416px;
    overflow: hidden;
    background: var(--banner-red);
  }
  .banner {
    position: relative;
    width: 1200px;
    height: 3416px;
    background: var(--banner-red);
    font-family: "M PLUS 1p", sans-serif;
  }
  .title-grid {
    position: absolute;
    left: 358px;
    top: 468px;
    width: 484px;
    height: 1444px;
    padding: 4px;
    gap: 4px;
    display: grid;
    grid-template-columns: 236px 236px;
    grid-template-rows: repeat(6, 236px);
    grid-auto-flow: column;
    background: var(--label-tan);
  }
  .title-grid .cell {
    display: flex;
    align-items: center;
    justify-content: center;
    background: var(--banner-red);
    color: var(--label-tan);
    font-size: 164px;
    font-weight: 300;
    line-height: 1;
  }
  .craft-photo {
    position: absolute;
    left: 0;
    top: 2428px;
    width: 1200px;
    height: 988px;
    background:
      radial-gradient(ellipse 45% 40% at 50% 45%, var(--photo-light) 0%, transparent 70%),
      linear-gradient(160deg, var(--photo-dark) 0%, var(--photo-mid) 55%, var(--photo-dark) 100%);
  }
</style>
</head>
<body>
  <div class="banner">
    <div class="title-grid">
      <span class="cell tagline">木</span>
      <span class="cell tagline">の</span>
      <span class="cell tagline">香</span>
      <span class="cell tagline">る</span>
      <span class="cell tagline">町</span>
      <span class="cell tagline">並</span>
      <span class="cell org-name">山</span>
      <span class="cell org-name">城</span>
      <span class="cell org-name">建</span>
      <span class="cell org-name">具</span>
      <span class="cell org-name">組</span>
      <span class="cell org-name">合</span>
    </div>
    <div class="craft-photo" role="img" aria-label="職人の両手が麻の葉模様の組子細工を差し出す写真"></div>
  </div>
</body>
</html>
```